Book cover design for a collection of poetry - The Lanternfield

Book cover and back design need to be moody, nostalgic, reflective, ethereal. Melancholy and other worldly. Cover design should not be time specific to a period or place but if applicable should reflect British landscape. Book cover should be in tones of blue and must include the title and author (THE LANTERNFIELD BY DORIAN WELKBRIDGE). We love the idea of rain, and looking out of a window. See attached designs. A world you are observing but not in.

Industry/Entity Type

Book Publisher

Font styles to use
Serif
Script

Colors
3176b5
3377b5
85acd3
eaf1f7
0792cd
33a6d7
86cae7
ecf7fb
86cfc6

Requirements
Must have
• The colour blue in it, must be melancholy and reflective.
Nice to have
• Rain in the cover.
Should not have
• Any bright colours.

```html
<!DOCTYPE html>
<html lang="en">
<head>
<meta charset="utf-8">
<title>The Lanternfield — Cover and Back</title>
<link rel="stylesheet" href="https://fonts.googleapis.com/css2?family=Cinzel:wght@400;500&family=Cormorant+Garamond:wght@500&family=Open+Sans:wght@400&display=swap">
<style>
  :root {
    --stage: #f1f1f1;
    --ink-black: #050607;
    --cover-dark: #04090b;
    --glow-cyan: #7fe3f2;
    --glow-teal: #2b98ac;
    --shadow-teal: #0c3640;
    --title-fill: #0a1417;
    --title-edge: #9fdbe6;
    --back-text: #86cae7;
    --back-heading: #a6dcea;
    --author: #9fb6bb;
  }
  * { margin: 0; padding: 0; box-sizing: border-box; }
  html, body {
    width: 1200px; height: 800px; overflow: hidden;
    background: var(--stage);
  }
  .spread {
    position: relative; width: 1200px; height: 800px;
    display: flex; justify-content: center; align-items: center; gap: 40px;
  }
  .back-cover, .front-cover {
    position: relative; width: 400px; height: 610px; overflow: hidden;
    box-shadow: 0 12px 30px rgba(0,0,0,0.25);
  }
  /* Back cover */
  .back-cover {
    background: var(--ink-black);
    text-align: center;
    padding: 90px 34px 0;
  }
  .back-heading {
    font-family: "Cinzel", "Times New Roman", serif;
    font-weight: 400; font-size: 21px; line-height: 1.3;
    letter-spacing: 0.06em; color: var(--back-heading);
  }
  .blurb {
    margin-top: 48px;
    font-family: "Open Sans", Arial, sans-serif;
    font-size: 8.6px; line-height: 1.55; letter-spacing: 0.03em;
    color: var(--back-text); text-transform: uppercase;
  }
  .blurb + .blurb { margin-top: 16px; }
  /* Front cover */
  .front-cover { background: var(--cover-dark); }
  .cover-scene {
    position: absolute; inset: 0;
    background:
      radial-gradient(ellipse 30% 36% at 50% 70%, var(--glow-cyan) 0%, var(--glow-teal) 45%, transparent 80%),
      radial-gradient(ellipse 60% 70% at 48% 62%, var(--shadow-teal) 0%, transparent 75%),
      linear-gradient(90deg, #020405 0%, #0b2329 45%, #0a1c21 60%, #020405 100%);
  }
  .cover-title {
    position: absolute; top: 70px; left: 0; right: 0;
    text-align: center;
    font-family: "Cinzel", "Times New Roman", serif;
    font-weight: 500; line-height: 1.05;
    color: var(--title-fill);
    -webkit-text-stroke: 1px var(--title-edge);
    text-shadow: 0 0 8px rgba(127,227,242,0.45);
  }
  .cover-title .line-small { display: block; font-size: 38px; letter-spacing: 0.04em; }
  .cover-title .line-large { display: block; font-size: 39px; letter-spacing: 0.03em; }
  .cover-author {
    position: absolute; bottom: 78px; left: 0; right: 0;
    text-align: center;
    font-family: "Cormorant Garamond", Georgia, serif;
    font-weight: 500; font-size: 14px; color: var(--author);
  }
</style>
</head>
<body>
  <main class="spread">
    <section class="back-cover" aria-label="Back cover">
      <h2 class="back-heading">THE LANTERNFIELD<br>IS A<br>COLLECTION OF POEMS</h2>
      <p class="blurb">
        Told in two parts we first meet Edward, an old man,<br>
        aged, crippled and left alone in his chair by the window,<br>
        reflecting on his life and his marriage to Alice.<br>
        In part two, Alice is suicidal, manically depressed and trapped in<br>
        life as a wife and mother. She meets, half in a dream, a young<br>
        soldier during WWII and her life is changed<br>
        forever.
      </p>
      <p class="blurb">
        Moving through the 20th century, this collection<br>
        interweaves grief, loss, longing,<br>
        mental illness, and ultimately the hope of love.
      </p>
    </section>

    <section class="front-cover" aria-label="Front cover">
      <div class="cover-scene" role="img" aria-label="Photograph of a rain-streaked four-pane window glowing blue in a dark weathered wall"></div>
      <h1 class="cover-title">
        <span class="line-small">THE</span>
        <span class="line-large">LANTERNFIELD</span>
      </h1>
      <p class="cover-author">Dorian Welkbridge</p>
    </section>
  </main>
</body>
</html>
```